I am a pastry chef and just started my own business. I make all sorts of pastries: french macarons, petit fours, artisan chocolates, artisan bread, and they can be ordered on the website. I'm obsessed with Wonderland, so I'd like to have a logo & a background that incorporate that, something whimsical. I was thinking of a white rabbit wearing a chef toque - maybe he could have a monocle on. The logo could go on one side of the business card with "Sugar Fox Patisserie Co" on a banner of some sort at the bottom, and the contact & info could go on the other side. I'd like a really light color as the background, maybe a really light yellow.

Industry/Entity Type

Chef

Contact Information for Business Card

Sugar Fox Patisserie Co
Mira Delcour Penhale
sugarfoxpatisserieco.shopvaleo.example
sugarfoxpatisserieco@mailvaleo.example
514-83-2071

```html
<!DOCTYPE html>
<html lang="en">
<head>
<meta charset="utf-8">
<title>Sugar Fox Patisserie Co — Business Card</title>
<link rel="stylesheet" href="https://fonts.googleapis.com/css2?family=Amaranth:wght@400;700&display=swap">
<style>
  :root {
    --backdrop: #ece3d3;
    --card: #f8efac;
    --ink: #7b1519;
    --icon-ink: #f8efac;
    --shadow: rgba(60, 40, 20, 0.35);
  }
  * { margin: 0; padding: 0; box-sizing: border-box; }
  html, body {
    width: 969px;
    height: 1200px;
    overflow: hidden;
    background: var(--backdrop);
  }
  .canvas {
    position: relative;
    width: 969px;
    height: 1200px;
    font-family: "Amaranth", sans-serif;
    color: var(--ink);
  }
  .card {
    position: absolute;
    width: 739px;
    height: 456px;
    background: var(--card);
    box-shadow: 0 6px 14px var(--shadow);
  }
  .card--front { left: 48px; top: 80px; }
  .card--back { left: 162px; top: 618px; }

  .rule-set {
    position: absolute;
    left: 0;
    width: 739px;
    height: 456px;
    top: 0;
    pointer-events: none;
  }
  .rule-set line {
    stroke: var(--ink);
    stroke-linecap: round;
  }

  .logo-mark {
    position: absolute;
    left: 290px;
    top: 70px;
    width: 160px;
    height: 160px;
    border: 4px solid var(--ink);
    border-radius: 50%;
  }
  .banner-name {
    position: absolute;
    left: 0;
    width: 739px;
    top: 340px;
    text-align: center;
    font-weight: 700;
    font-size: 44px;
    line-height: 1;
  }

  .contact-panel {
    position: absolute;
    left: 0;
    top: 64px;
    width: 86px;
    height: 166px;
    background: var(--ink);
  }
  .contact-icon {
    position: absolute;
    left: 28px;
    width: 38px;
    height: 38px;
  }
  .contact-icon * {
    fill: none;
    stroke: var(--icon-ink);
    stroke-width: 2.6;
  }
  .contact-icon .solid { fill: var(--icon-ink); stroke: none; }
  .icon-web { top: 10px; }
  .icon-mail { top: 66px; }
  .icon-phone { top: 119px; }

  .contact-line {
    position: absolute;
    left: 101px;
    font-size: 25px;
    font-weight: 700;
    line-height: 1;
  }
  .contact-line--web { top: 80px; }
  .contact-line--mail { top: 137px; }
  .contact-line--phone { top: 190px; }

  .person-name {
    position: absolute;
    right: 35px;
    top: 322px;
    font-size: 40px;
    font-weight: 700;
    line-height: 1;
  }
  .person-company {
    position: absolute;
    right: 35px;
    top: 392px;
    font-size: 27px;
    font-weight: 700;
    line-height: 1;
  }
</style>
</head>
<body>
<main class="canvas">

  <section class="card card--front" aria-label="Business card front">
    <div class="logo-mark" aria-hidden="true"></div>
    <svg class="rule-set" viewBox="0 0 739 456" aria-hidden="true">
      <line x1="0" y1="327" x2="739" y2="325" stroke-width="3" stroke-dasharray="60 3 25 2 90 4 40 2"/>
      <line x1="0" y1="333" x2="739" y2="332" stroke-width="1.5" stroke-dasharray="30 6 70 4 20 5"/>
      <line x1="0" y1="407" x2="739" y2="405" stroke-width="3" stroke-dasharray="80 3 30 2 55 4 20 2"/>
      <line x1="0" y1="413" x2="739" y2="412" stroke-width="1.5" stroke-dasharray="45 5 25 6 60 4"/>
    </svg>
    <h1 class="banner-name">Sugar Fox Patisserie Co</h1>
  </section>

  <section class="card card--back" aria-label="Business card back">
    <div class="contact-panel">
      <svg class="contact-icon icon-web" viewBox="0 0 38 38" aria-hidden="true">
        <circle cx="19" cy="19" r="15"/>
        <ellipse cx="19" cy="19" rx="7" ry="15"/>
        <line x1="4" y1="19" x2="34" y2="19"/>
        <line x1="7" y1="11" x2="31" y2="11"/>
        <line x1="7" y1="27" x2="31" y2="27"/>
      </svg>
      <svg class="contact-icon icon-mail" viewBox="0 0 38 38" aria-hidden="true">
        <rect x="4" y="9" width="30" height="20"/>
        <polyline points="4,9 19,21 34,9"/>
      </svg>
      <svg class="contact-icon icon-phone" viewBox="0 0 38 38" aria-hidden="true">
        <path class="solid" d="M10 5 L15 5 L17 13 L13 16 C15 21 18 24 23 26 L26 22 L34 24 L34 29 C34 32 31 34 28 33 C16 30 8 22 5 10 C4 7 6 5 10 5 Z"/>
      </svg>
    </div>
    <p class="contact-line contact-line--web">sugarfoxpatisserieco.shopvaleo.example</p>
    <p class="contact-line contact-line--mail">sugarfoxpatisserieco@mailvaleo.example</p>
    <p class="contact-line contact-line--phone">514-83-2071</p>

    <svg class="rule-set" viewBox="0 0 739 456" aria-hidden="true">
      <line x1="0" y1="300" x2="739" y2="298" stroke-width="3" stroke-dasharray="70 3 30 2 85 4 35 2"/>
      <line x1="0" y1="307" x2="739" y2="306" stroke-width="1.5" stroke-dasharray="35 6 60 4 25 5"/>
      <line x1="0" y1="380" x2="739" y2="378" stroke-width="3" stroke-dasharray="55 3 40 2 75 4 25 2"/>
      <line x1="0" y1="387" x2="739" y2="386" stroke-width="1.5" stroke-dasharray="40 5 30 6 55 4"/>
      <line x1="0" y1="428" x2="739" y2="426" stroke-width="3" stroke-dasharray="65 3 35 2 80 4 30 2"/>
    </svg>
    <h2 class="person-name">Mira Delcour Penhale</h2>
    <p class="person-company">Sugar Fox Patisserie Co</p>
  </section>

</main>
</body>
</html>
```